The Vixen Rides Again Line of Sparkling Wine & Spirits

Back info: Tara Rose Whitfield Owner 209-555-0143 1480 E. Harlow Rd, Bldg. 7, & 8, Lodi Ca. 95299
Sparkling Wines & Memorabilia www.thevixenridesagain.example
Ok I have uploaded the winning design. The color that I am after is the Fushia, Raspberry, Red, Matte Satin Matalic Finish. With a 24 Karet Gold color Foil. The Bottle is on the top row and it's the 2nd Bottle in. That is the Color that I want. This is the style of font. Make sure that you put what we're advertising. Good Luck to you all. Warmest regards, Tara
Target Market(s)
21 & up UniSex
Industry/Entity Type
Sparkling Wine and Memorabilia
Contact Information for Business Card
there listed up above.....

```html
<!DOCTYPE html>
<html lang="en">
<head>
<meta charset="utf-8">
<title>The Vixen Rides Again — Business Card</title>
<link rel="stylesheet" href="https://fonts.googleapis.com/css2?family=Montserrat:wght@400;500;600&family=Pinyon+Script&display=swap">
<style>
  :root {
    --stage: #1c1c1c;
    --ink: #000000;
    --fuchsia: #e2168f;
    --fuchsia-deep: #cf1282;
    --fuchsia-shade: #d81488;
    --paper: #ffffff;
    --gold: #d9a83a;
  }
  * { margin: 0; padding: 0; box-sizing: border-box; }
  html, body {
    width: 1200px; height: 1015px; overflow: hidden;
    background: var(--stage);
    font-family: "Montserrat", Arial, sans-serif;
  }
  .stage {
    position: relative; width: 1200px; height: 1015px;
    display: flex; flex-direction: column; align-items: center; justify-content: center; gap: 46px;
  }
  .card {
    position: relative; width: 760px; height: 434px; overflow: hidden;
    background: var(--ink);
    box-shadow: 0 14px 30px rgba(0,0,0,.55);
  }
  .card-bg { position: absolute; inset: 0; width: 100%; height: 100%; }
  .brand {
    position: absolute; left: 60px; top: 292px;
    color: var(--gold); font-weight: 600; font-size: 44px; letter-spacing: .5px; line-height: 1;
  }
  .tagline {
    position: absolute; left: 62px; top: 354px;
    color: var(--gold); font-weight: 500; font-size: 19px; letter-spacing: 1.5px;
  }
  .person-name {
    position: absolute; left: 44px; top: 240px;
    font-family: "Pinyon Script", cursive; color: var(--gold);
    font-size: 40px; font-weight: 400; line-height: 1;
  }
  .person-role {
    position: absolute; left: 48px; top: 288px;
    color: var(--gold); font-size: 16px; font-weight: 400; line-height: 20px;
  }
  .contact-list {
    position: absolute; left: 48px; top: 314px; list-style: none;
    color: var(--gold); font-size: 15px; line-height: 23px;
  }
  .contact-list li { display: flex; align-items: center; gap: 10px; }
  .contact-list svg { width: 14px; height: 14px; flex: none; }
  .address {
    position: absolute; left: 48px; top: 388px;
    color: var(--gold); font-size: 15px; line-height: 19px;
  }
  .address span { display: block; }
  .bottle-art {
    position: absolute; right: 48px; top: 18px; width: 92px; height: 395px;
    border-radius: 30px 30px 22px 22px;
    background: linear-gradient(90deg, #a30c62, var(--fuchsia) 45%, #f04aa8 60%, #b50d6c);
  }
</style>
</head>
<body>
<main class="stage">

  <section class="card card-front" aria-label="Card front">
    <svg class="card-bg" viewBox="0 0 760 434" preserveAspectRatio="none" aria-hidden="true">
      <path d="M0 0 H760 V180 C690 250 600 200 470 200 C300 200 150 230 0 280 Z" fill="var(--fuchsia)"/>
      <path d="M150 0 H760 V120 C650 170 520 140 380 140 C280 140 210 90 150 0 Z" fill="var(--fuchsia-shade)" opacity=".6"/>
      <path d="M400 0 H760 V70 C660 105 540 80 460 50 C430 35 410 20 400 0 Z" fill="var(--fuchsia-deep)" opacity=".5"/>
    </svg>
    <h1 class="brand">The Vixen Rides Again</h1>
    <p class="tagline">SPARKLING WINES &amp; MEMORABILIA</p>
  </section>

  <section class="card card-back" aria-label="Card back">
    <svg class="card-bg" viewBox="0 0 760 434" preserveAspectRatio="none" aria-hidden="true">
      <rect x="0" y="0" width="760" height="434" fill="var(--paper)"/>
      <path d="M0 70 C200 50 380 110 520 160 C620 195 700 192 760 188 V230 C650 215 520 205 420 208 C260 212 120 235 0 262 V434 H760 V0 Z" fill="none"/>
      <path d="M0 70 C200 50 380 110 520 160 C620 195 700 192 760 188 V434 H0 Z" fill="var(--fuchsia)"/>
      <path d="M0 70 C200 50 380 110 520 160 C560 174 600 182 640 186 C520 190 380 150 240 110 C150 88 70 84 0 92 Z" fill="var(--fuchsia-deep)" opacity=".6"/>
      <path d="M760 230 C650 215 520 205 420 208 C260 212 120 235 0 262 V434 H760 Z" fill="var(--ink)"/>
    </svg>
    <div class="bottle-art" role="img" aria-label="Illustration of a fuchsia sparkling wine bottle with gold neck band and crest label"></div>
    <h2 class="person-name">Tara Rose Whitfield</h2>
    <p class="person-role">Owner</p>
    <ul class="contact-list">
      <li>
        <svg viewBox="0 0 24 24" aria-hidden="true"><path fill="var(--gold)" d="M6.6 10.8a15 15 0 0 0 6.6 6.6l2.2-2.2a1 1 0 0 1 1-.25 11.4 11.4 0 0 0 3.6.57 1 1 0 0 1 1 1V20a1 1 0 0 1-1 1A17 17 0 0 1 3 4a1 1 0 0 1 1-1h3.5a1 1 0 0 1 1 1c0 1.25.2 2.45.57 3.6a1 1 0 0 1-.25 1z"/></svg>
        209-555-0143
      </li>
      <li>
        <svg viewBox="0 0 24 24" aria-hidden="true"><path fill="var(--gold)" d="M2 5h20v14H2z"/><path d="M2 5l10 8 10-8" fill="none" stroke="var(--ink)" stroke-width="2"/></svg>
        thequeen@thevixenridesagain.example
      </li>
      <li>
        <svg viewBox="0 0 24 24" aria-hidden="true"><g fill="none" stroke="var(--gold)" stroke-width="2"><circle cx="12" cy="12" r="9"/><path d="M3 12h18M12 3c3 3 3 15 0 18M12 3c-3 3-3 15 0 18"/></g></svg>
        www.thevixenridesagain.example
      </li>
    </ul>
    <p class="address">
      <span>1480 E. Harlow Rd</span>
      <span>Bldg. 7, &amp; 8, Lodi Ca. 95299</span>
    </p>
  </section>

</main>
</body>
</html>
```